Financial Planning Pyramid Graphic

I need a graphic of a pyramid including 3 levels.

I've attached a copy of the article to be published with the graphic.

Also attached company logos if it makes sense to use.

See www.NovalisCapitalAdvisors.com for a general reference.

Target Market(s)

small and medium size business owners who intend to eventually sell their business. primarily servicing the construction, real estate, and technology industries.

Industry/Entity Type

Financial Planning

Font styles to use
Sans Serif

Requirements
Must have
• Primary branding hex color #009b81

Three levels of the pyramid:
3. Top: Wealth Distribution
2. Middle: Growing Wealth
1. Base: Protection (Risk Management)

It should somehow show how "Tax Planning" permeates all 3 layers.
Nice to have
• The attached article includes details about what the graphic should represent and more details that may be included.

```html
<!DOCTYPE html>
<html lang="en">
<head>
<meta charset="utf-8">
<title>Financial Planning Pyramid – Novalis Capital Advisors</title>
<link href="https://fonts.googleapis.com/css2?family=Bebas+Neue&display=swap" rel="stylesheet">
<style>
  :root {
    --brand: #009b81;
    --brand-deep: #0c5f6e;
    --mint-light: #e3f8f3;
    --mint-soft: #cfe9e3;
    --ink: #2c2f33;
    --label: #ffffff;
    --tax-label: #0f6f7c;
    --page: #ffffff;
    --rule: #9a9a9a;
  }
  html, body {
    margin: 0;
    padding: 0;
    width: 1200px;
    height: 614px;
    overflow: hidden;
    background: var(--page);
  }
  .canvas {
    position: relative;
    width: 1200px;
    height: 614px;
  }
  .artwork {
    display: block;
    width: 1200px;
    height: 614px;
  }
  .tier-label {
    font-family: "Bebas Neue", "Arial Narrow", sans-serif;
    fill: var(--label);
    font-size: 13px;
    letter-spacing: 0.2px;
    text-anchor: middle;
  }
  .tax-label {
    font-family: "Bebas Neue", "Arial Narrow", sans-serif;
    fill: var(--tax-label);
    font-size: 13px;
    letter-spacing: 0.3px;
  }
  .brand-name {
    font-family: "Bebas Neue", "Arial Narrow", sans-serif;
    fill: var(--ink);
    text-anchor: middle;
  }
  .brand-name__main { font-size: 30px; letter-spacing: 3px; }
  .brand-name__sub { font-size: 11px; letter-spacing: 2.4px; }
  .base-rule { stroke: var(--rule); stroke-width: 1; }
</style>
</head>
<body>
<main class="canvas">
  <svg class="artwork" viewBox="0 0 1165 596" xmlns="http://www.w3.org/2000/svg" aria-labelledby="title">
    <title id="title">Financial planning pyramid: protection, growing wealth and wealth distribution, with tax planning running through all three levels</title>
    <defs>
      <linearGradient id="tier-top" x1="0" y1="0" x2="0" y2="1">
        <stop offset="0" stop-color="#6cf0d0"/>
        <stop offset="0.55" stop-color="#25b79b"/>
        <stop offset="1" stop-color="#1b8f83"/>
      </linearGradient>
      <linearGradient id="tier-middle" x1="0" y1="0" x2="0" y2="1">
        <stop offset="0" stop-color="#009b81"/>
        <stop offset="0.6" stop-color="#1a9c93"/>
        <stop offset="1" stop-color="#2aa3a6"/>
      </linearGradient>
      <linearGradient id="tier-base" x1="0" y1="0" x2="0" y2="1">
        <stop offset="0" stop-color="#0c5f6e"/>
        <stop offset="0.6" stop-color="#1a7488"/>
        <stop offset="1" stop-color="#2a8aa2"/>
      </linearGradient>
      <linearGradient id="tax-cloud" x1="0" y1="0" x2="0" y2="1">
        <stop offset="0" stop-color="#e6faf5"/>
        <stop offset="1" stop-color="#cbe7e0"/>
      </linearGradient>
      <linearGradient id="tax-wedge" x1="0" y1="0" x2="1" y2="0">
        <stop offset="0" stop-color="#e2f6f1"/>
        <stop offset="1" stop-color="#c7ebe3"/>
      </linearGradient>
      <linearGradient id="light-beam" x1="0" y1="0" x2="0" y2="1">
        <stop offset="0" stop-color="#ffffff" stop-opacity="0.28"/>
        <stop offset="1" stop-color="#ffffff" stop-opacity="0"/>
      </linearGradient>
      <filter id="tier-shadow" x="-10%" y="-10%" width="120%" height="130%">
        <feDropShadow dx="3" dy="4" stdDeviation="3" flood-color="#0b3b40" flood-opacity="0.35"/>
      </filter>
      <filter id="floor-blur" x="-20%" y="-200%" width="140%" height="500%">
        <feGaussianBlur stdDeviation="6"/>
      </filter>
    </defs>

    <!-- Brand -->
    <g class="brand" aria-label="Novalis Capital Advisors">
      <text class="brand-name brand-name__main" x="580" y="58">NOVALIS</text>
      <text class="brand-name brand-name__sub" x="580" y="76">CAPITAL ADVISORS</text>
    </g>

    <!-- Left pyramid: tax planning as a surrounding field -->
    <g class="pyramid pyramid--field">
      <path class="tax-field" fill="url(#tax-cloud)"
        d="M210 155 C230 135 330 140 380 138 C420 137 418 170 392 190 C372 206 405 225 440 232
           C500 245 520 265 500 292 C485 315 470 345 520 360 C565 374 575 405 555 425
           C540 440 505 450 470 448 L150 445 C110 448 80 430 75 405 C70 380 85 360 80 340
           C75 318 45 300 38 272 C32 248 60 238 110 238 C160 238 220 230 235 212
           C248 196 195 180 210 155 Z"/>
      <text class="tax-label" x="110" y="292">TAX PLANNING</text>

      <ellipse cx="311" cy="515" rx="200" ry="8" fill="#9b9b9b" opacity="0.55" filter="url(#floor-blur)"/>

      <g filter="url(#tier-shadow)">
        <polygon fill="url(#tier-base)" points="145,358 477,358 517,474 106,474"/>
        <polygon fill="url(#tier-middle)" points="238,229 385,229 443,336 179,336"/>
        <polygon fill="url(#tier-top)" points="311,92 374,208 247,208"/>
      </g>
      <text class="tier-label" x="311" y="163">WEALTH</text>
      <text class="tier-label" x="311" y="180">DISTRIBUTION</text>
      <text class="tier-label" x="311" y="289">GROWING WEALTH</text>
      <text class="tier-label" x="311" y="429">PROTECTION (RISK MANAGEMENT)</text>
    </g>

    <!-- Right pyramid: tax planning as a supporting wedge -->
    <g class="pyramid pyramid--wedge">
      <polygon class="tax-wedge" fill="url(#tax-wedge)" points="845,92 1070,474 845,474"/>
      <text class="tax-label" transform="translate(954 248) rotate(60)">TAX PLANNING</text>

      <ellipse cx="845" cy="515" rx="200" ry="8" fill="#9b9b9b" opacity="0.55" filter="url(#floor-blur)"/>

      <g filter="url(#tier-shadow)">
        <polygon fill="url(#tier-base)" points="679,358 1012,358 1050,474 640,474"/>
        <polygon fill="url(#tier-middle)" points="778,229 912,229 977,336 713,336"/>
        <polygon fill="url(#tier-top)" points="845,92 908,208 781,208"/>
      </g>
      <polygon class="light-beam" fill="url(#light-beam)" points="795,229 815,229 775,474 745,474"/>
      <text class="tier-label" x="845" y="163">WEALTH</text>
      <text class="tier-label" x="845" y="180">DISTRIBUTION</text>
      <text class="tier-label" x="845" y="289">GROWING WEALTH</text>
      <text class="tier-label" x="845" y="429">PROTECTION (RISK MANAGEMENT)</text>
    </g>

    <line class="base-rule" x1="0" y1="594.5" x2="1165" y2="594.5"/>
  </svg>
</main>
</body>
</html>
```